Medical Centre Trifold Brochure

New Medical Centre needs a bright and airy Trifold brochure. We want to introduce our practice to the surrounding area so want to advise our services and introduce the Doctors and Nurses.

I will upload all the pictures and logos, along with some pdf pages of styles that we like (and some we dont) to assist your creativity.

We will provide as much feedback for you as possible.

After this project, we would like to work with the same designer to expand into some other brochures etc that we have in mind, so this is a starting point.

Hi Designers,

We are looking forward to seeing yuor work. Are you happy that you have enough information to get started?

Please let me know if you need anything else?

Cheers

Hi Designers.. I should mention the brochure itself.. we are looking for a doubled sided, full colour brochure that will be folded into thirds so it becomes a DL size.. I hope that makes sense.

Any questions always welcome.

Target Market(s)

Females - Mothers / Wives / Grandmothers

Industry/Entity Type

Medical

Requirements
Must have
• Tri Fold Medical – Larkvale Family Health

• Include images of the Doctors (I will supply) and the Nursing Staff

• “Chunks” of information
o Introduction to who we are (I will supply)
o Our services (I will supply)
o Fee’s
• We are a newly renovated Medical Clinic
• Plotwise Map of our location – Photo of the outside of the centre near the plotwise map
• Opening Hours
• Contact Details / website address www.larkvalefamilyhealth.com.au (not yet live but must be included)
• Interior Reception area photo
• Ask a question.. “Are you worried about your patient history?.. We can help”
• Need to leave a space for a Magnet.. (business card sized)

3 Doctor Photos (2 uploaded already)
Image of the centre (uploaded already)

I will upload a detailed description of what we are looking for.
Nice to have
• Photo's of 2 Nurses (1 already uploaded - Maren)

```html
<!DOCTYPE html>
<html lang="en">
<head>
<meta charset="utf-8">
<title>Larkvale Family Health – Trifold Brochure</title>
<link href="https://fonts.googleapis.com/css2?family=Arimo:ital,wght@0,400;0,700;1,700&family=Poiret+One&display=swap" rel="stylesheet">
<style>
  :root{
    --backdrop:#9a9b9f;
    --paper:#ffffff;
    --green:#8cc63f;
    --green-deep:#5fb84a;
    --lime:#b5d334;
    --yellow:#f1e600;
    --ink:#4d4d4f;
    --grey-photo:#9c9c9c;
  }
  *{margin:0;padding:0;box-sizing:border-box}
  html,body{width:1200px;height:900px;overflow:hidden;background:var(--backdrop)}
  body{position:relative;font-family:"Arimo",Arial,sans-serif;color:var(--ink)}
  .sheet{position:absolute;left:37px;top:48px;width:1128px;height:802px;background:var(--paper);overflow:hidden}
  .abs{position:absolute}

  .fees{left:23px;top:45px;width:344px;height:480px;border:3px solid var(--green);border-radius:16px;overflow:hidden;background:var(--paper)}
  .fees-title{position:absolute;left:9px;top:16px;font-weight:700;font-size:23px;color:#5aa133}
  .fees-body{position:absolute;left:0;top:47px;right:0;bottom:0;background:linear-gradient(180deg,var(--lime) 0%,#84c441 60%,var(--green-deep) 100%)}
  .fees-divider{position:absolute;left:216px;top:9px;bottom:9px;width:1.5px;background:#fff}
  .fees-list{position:absolute;left:8px;top:11px;width:320px;list-style:none;color:#fff;font-size:12.5px}
  .fees-list li{display:flex;height:18.4px;align-items:center}
  .fees-list .service{width:232px}

  .map{left:390px;top:22px;width:346px;height:292px;background:linear-gradient(135deg,#e9e7e1,#dcdad3)}
  .info{left:390px;top:325px;width:346px;text-align:center;font-size:13px;line-height:16px;color:#4a4a4a}
  .info .address,.info .contact{margin-bottom:17px}
  .info .contact{margin-bottom:27px}

  .brand-mark{left:796px;top:112px;width:34px;height:34px;background:var(--green)}
  .brand-name{left:794px;top:218px;width:300px;font-family:"Poiret One","Arimo",sans-serif;font-weight:400;font-size:46px;line-height:66px;color:var(--ink)}
  .brand-rule{left:796px;top:382px;width:274px;height:1.5px;background:var(--green)}
  .brand-services{left:800px;top:389px;width:280px;font-size:20px;letter-spacing:3.2px;color:var(--ink);white-space:nowrap}

  .photo{position:absolute}
  .photo-silhouette{left:100px;top:550px;width:106px;height:125px;background:var(--grey-photo);border-radius:50px 50px 8px 8px}
  .photo-nurse{left:206px;top:560px;width:106px;height:125px;background:linear-gradient(180deg,#e5c7a8 0%,#f2f2f2 60%,#ffffff 100%);border-radius:44px 44px 6px 6px}
  .photo-centre{left:380px;top:557px;width:368px;height:145px;background:linear-gradient(180deg,#c9cbcf 0%,#a9553c 35%,#b3614a 100%)}
  .photo-doctors{left:918px;top:440px;width:182px;height:170px;background:linear-gradient(180deg,#6b5a4c 0%,#e3c2a6 35%,#b9b7b0 100%);border-radius:60px 60px 0 0}

  .swoosh{left:0;top:0;width:1128px;height:802px}

  .nurse-name{left:231px;top:690px;font-weight:700;font-style:italic;font-size:16px;color:#fff}
  .slogan{left:760px;top:665px;width:344px;text-align:center;font-weight:700;font-style:italic;font-size:24px;line-height:28px;color:var(--yellow)}
  .website{left:0;top:746px;width:1122px;text-align:center;font-size:15px;color:#fff}
</style>
</head>
<body>
<main class="sheet">

  <section class="fees abs">
    <h2 class="fees-title">FEES</h2>
    <div class="fees-body">
      <span class="fees-divider"></span>
      <ul class="fees-list">
        <li><span class="service">Medical Care</span><span>AUD&nbsp;&nbsp;700</span></li>
        <li><span class="service">Dental</span><span>AUD 1000</span></li>
        <li><span class="service">Operation Tooth</span><span>AUD 450</span></li>
        <li><span class="service">Phschology</span><span>AUD 1250</span></li>
        <li><span class="service">Physiotherapy</span><span>AUD&nbsp;&nbsp;700</span></li>
        <li><span class="service">Consultation</span><span>AUD 1000</span></li>
        <li><span class="service">Theraphy</span><span>AUD 450</span></li>
        <li><span class="service">Medical Care</span><span>AUD&nbsp;&nbsp;700</span></li>
        <li><span class="service">Dental</span><span>AUD 1000</span></li>
        <li><span class="service">Operation Tooth</span><span>AUD 450</span></li>
        <li><span class="service">Phschology</span><span>AUD 1250</span></li>
        <li><span class="service">Physiotherapy</span><span>AUD&nbsp;&nbsp;700</span></li>
        <li><span class="service">Consultation</span><span>AUD 1000</span></li>
        <li><span class="service">Theraphy</span><span>AUD 450</span></li>
        <li><span class="service">Medical Care</span><span>AUD&nbsp;&nbsp;700</span></li>
        <li><span class="service">Dental</span><span>AUD 1000</span></li>
        <li><span class="service">Operation Tooth</span><span>AUD 450</span></li>
        <li><span class="service">Phschology</span><span>AUD 1250</span></li>
        <li><span class="service">Physiotherapy</span><span>AUD&nbsp;&nbsp;700</span></li>
        <li><span class="service">Consultation</span><span>AUD 1000</span></li>
        <li><span class="service">Theraphy</span><span>AUD 450</span></li>
      </ul>
    </div>
  </section>

  <div class="map abs" role="img" aria-label="Plotwise map of the streets around the clinic with a location pin"></div>

  <section class="info abs">
    <p class="address">Address<br>18, 240 Larkvale Street, NSW 2150</p>
    <p class="contact">Contact<br>+61 555 010 020300</p>
    <p class="hours">Opening Hours<br>Weekdays : 9 am - 5 pm</p>
  </section>

  <div class="brand-mark abs"></div>
  <div class="brand-name abs">Larkvale<br>Family Health</div>
  <div class="brand-rule abs"></div>
  <div class="brand-services abs">•Medical&nbsp;&nbsp;•Dental</div>

  <div class="photo photo-silhouette" role="img" aria-label="Placeholder silhouette for a staff member photo"></div>
  <div class="photo photo-nurse" role="img" aria-label="Portrait photo of nurse Maren"></div>
  <div class="photo photo-centre" role="img" aria-label="Photo of the brick clinic exterior with Now Open signs"></div>
  <div class="photo photo-doctors" role="img" aria-label="Photo of two doctors, a woman and a man"></div>

  <svg class="swoosh abs" viewBox="0 0 1128 802" aria-hidden="true">
    <defs>
      <linearGradient id="band" x1="0" y1="0" x2="1" y2="0">
        <stop offset="0" stop-color="#8cc63f"/>
        <stop offset="0.35" stop-color="#d8e21a"/>
        <stop offset="0.5" stop-color="#f1e600"/>
        <stop offset="0.65" stop-color="#a9cf38"/>
        <stop offset="1" stop-color="#8cc63f"/>
      </linearGradient>
    </defs>
    <path d="M0,647 C260,668 520,700 740,660 C880,630 1030,540 1128,388 L1128,802 L0,802 Z" fill="#b6d52f"/>
    <path d="M0,647 C250,672 500,706 730,672 C900,640 1040,560 1128,470 L1128,802 L0,802 Z" fill="url(#band)"/>
    <path d="M0,700 C250,710 520,720 760,690 C920,660 1050,590 1128,520 L1128,802 L0,802 Z" fill="#8cc63f"/>
    <path d="M790,640 C930,600 1050,530 1128,455 L1128,470 C1050,548 940,610 790,640 Z" fill="#ffffff"/>
  </svg>

  <div class="nurse-name abs">MAREN</div>
  <div class="slogan abs">WE ARE<br>ALWAYS HERE TO HELP</div>
  <div class="website abs">www.larkvalefamilyhealth.com.au</div>

</main>
</body>
</html>
```